Oil Field Service company needs professional business cards

Looking to clean up our current company business cards and look a little more professional. Harlow Tubular Services is a US based company that services the oil field. We deal with engineers, managers and oil rigs....................................................................................................................................................................................................................................................................................................................................................................................................

Target Market(s)

Oil and Gas professionals

Industry/Entity Type

Oil And Gas

Contact Information for Business Card

See attached photo as example

Font styles to use
Sans Serif

Colors
ec1f27

Requirements
Must have
• Company Logo, Name, Title, Cell, Office, Fax, Email.
• See attached photo
Nice to have
• External CRT, Internal CRT, Casing Crews, Torque Turn, Laydown Machine
Should not have
• Do not introduce any new pictures and keep it professional looking

```html
<!DOCTYPE html>
<html lang="en">
<head>
<meta charset="utf-8">
<title>Harlow Tubular Services – Business Card</title>
<link href="https://fonts.googleapis.com/css2?family=Questrial&family=Ubuntu:wght@400&display=swap" rel="stylesheet">
<style>
  :root {
    --brand-red: #ec1f27;
    --band-red: #cf1f26;
    --slate: #44505c;
    --ink: #3d4148;
    --page: #9b9b9b;
    --card-light: #ffffff;
    --card-shade: #dcdcdc;
  }
  * { margin: 0; padding: 0; box-sizing: border-box; }
  html, body { width: 1200px; height: 965px; overflow: hidden; }
  body { background: var(--page); font-family: "Questrial", sans-serif; position: relative; }

  .card {
    position: absolute; left: 100px; top: 196px;
    width: 1000px; height: 572px;
    background: radial-gradient(ellipse at 72% 28%, var(--card-light) 0%, #f3f3f3 40%, var(--card-shade) 100%);
    overflow: hidden;
  }

  .wordmark { position: absolute; left: 53px; top: 62px; color: var(--slate); font-family: "Questrial", sans-serif; }
  .wordmark__main { display: block; font-size: 84px; line-height: 1; letter-spacing: 2px; text-transform: uppercase; }
  .wordmark__sub { display: block; font-size: 24px; letter-spacing: 6.2px; text-transform: uppercase; margin-top: 22px; padding-left: 4px; }

  .person { position: absolute; left: 53px; top: 236px; }
  .person__name { font-family: "Ubuntu", sans-serif; color: var(--brand-red); font-size: 33px; line-height: 1.1; }
  .person__title { color: var(--ink); font-size: 23px; line-height: 1.2; }

  .contacts { position: absolute; left: 53px; top: 327px; list-style: none; }
  .contacts li { display: flex; align-items: center; height: 29px; color: var(--ink); font-size: 23px; }
  .contacts svg { width: 24px; height: 22px; margin-right: 13px; fill: var(--brand-red); }

  .address { position: absolute; left: 53px; top: 464px; color: var(--ink); font-size: 23px; }

  .rule { position: absolute; left: 0; top: 516px; width: 100%; height: 5px; background: var(--slate); }
  .services {
    position: absolute; left: 0; top: 523px; width: 100%; height: 49px;
    background: var(--band-red); color: #fff; font-size: 23px;
    display: flex; align-items: center; justify-content: center;
  }
</style>
</head>
<body>
  <div class="card">
    <div class="wordmark">
      <span class="wordmark__main">Harlow</span>
      <span class="wordmark__sub">Tubular Services</span>
    </div>

    <div class="person">
      <div class="person__name">Wade Callister</div>
      <div class="person__title">Area Manager</div>
    </div>

    <ul class="contacts">
      <li>
        <svg viewBox="0 0 24 22" aria-hidden="true"><rect x="2" y="3" width="5" height="17" rx="1"/><rect x="8" y="1" width="14" height="19" rx="1"/><rect x="10" y="3" width="10" height="4" fill="#fff"/><rect x="10" y="9" width="2" height="2" fill="#fff"/><rect x="14" y="9" width="2" height="2" fill="#fff"/><rect x="18" y="9" width="2" height="2" fill="#fff"/><rect x="10" y="13" width="2" height="2" fill="#fff"/><rect x="14" y="13" width="2" height="2" fill="#fff"/><rect x="18" y="13" width="2" height="2" fill="#fff"/></svg>
        (555) 014 2200
      </li>
      <li>
        <svg viewBox="0 0 24 22" aria-hidden="true"><rect x="6" y="1" width="12" height="20" rx="2"/><rect x="8" y="4" width="8" height="12" fill="#fff"/><circle cx="12" cy="18.5" r="1.2" fill="#fff"/></svg>
        (555) 017 8341
      </li>
      <li>
        <svg viewBox="0 0 24 22" aria-hidden="true"><rect x="6" y="1" width="12" height="7"/><rect x="1" y="8" width="22" height="10" rx="2"/><rect x="5" y="15" width="14" height="6" fill="#fff" stroke="#ec1f27" stroke-width="1.5"/></svg>
        (555) 014 2290
      </li>
      <li>
        <svg viewBox="0 0 24 22" aria-hidden="true"><rect x="1" y="4" width="22" height="15"/><path d="M1 4 L12 13 L23 4" fill="none" stroke="#fff" stroke-width="1.8"/><path d="M1 19 L9 11 M23 19 L15 11" stroke="#fff" stroke-width="1.5"/></svg>
        wcallister@harlowtubular.com
      </li>
    </ul>

    <div class="address">Elk Ridge, OK 73640</div>

    <div class="rule"></div>
    <div class="services">External CRT, Internal CRT, Casing Crews, Torque Turn, Laydown Machine</div>
  </div>
</body>
</html>
```